The Marisol & Jocelyn Fruit Co.

We produce a very high quality freeze dried fruit, all organic, no preservative, no additives, nothing but the fruit. To get more use out of a facility we have in Charlotte, we decided to pursue some high end online retailers with a high end freeze dried organic fruit. We are looking for a very high end, upper east side, trendy, hip, logo and package design for this. There are 4 SKU's - Freeze Dried Strawberries, Freeze Dried Blueberries, Freeze Dried Cherries, and a blend of of all 3 as the 4th SKU. 2 labels each that are 6" x 6" - The front, again needs to be fun and trendy big bold etc. Nothing frilly and Quiet Barn by the creek. The back needs to contain the nutritional statements for each and some copy describing the product and the company.
Updates
This would be one of only a few competitors in this segment
We are looking to steal a page from the wine industry. The coolest looking label on the shelf wins over the uneducated wine buyer. The designs are all fine, but they need to be sleeker, sexier, funner, etc. Someone should look at the label and say....wow that is FUN AND SEXY! I have to buy some! VORBEX.COM screams that. Don't worry so much about pictures of the fruit as the bag is going to be clear. Sell the brand not the fruit. OK?
Reason: Why not?
Reason: Final Selection by Monday 5pm EST.
For all designs that have not been eliminated:
Reason: Final selections. All four designs front and back on one file uploaded by noon tomorrow ( 12:01 PM EST New York)
Target Market(s)
People that would shop at sites like www.vorbex.com
Industry/Entity Type
It Company
Requirements
Nice to have
- The brand is named after our two daughters - One is very girly and the other is very "sassy" It would be fun to have the logo capture their personalities a little. I have uploaded a picture. Marisol on the left, Jocelyn on the right.
Also, another of our brands, Hank Pellow, packaging is attached here. Some consistency in look and feel may be good.
Should not have
- Nothing frilly or dainty, or delicate. Colorful fun and bold but trendy.

```html
<!DOCTYPE html>
<html lang="en">
<head>
<meta charset="utf-8">
<title>Marisol &amp; Jocelyn Fruit Co — Freeze Dried Fruit Labels</title>
<link rel="stylesheet" href="https://fonts.googleapis.com/css2?family=Jost:wght@300;400&family=Ubuntu+Mono&display=swap">
<style>
  :root {
    --canvas: #ffffff;
    --lid: #bdb829;
    --body: #c8c430;
    --white: #ffffff;
    --blueberry: #00b5e9;
    --cherry: #c4161c;
    --shadow: rgba(0, 0, 0, 0.35);
  }
  * { margin: 0; padding: 0; box-sizing: border-box; }
  html, body { width: 1200px; height: 644px; overflow: hidden; background: var(--canvas); }
  .canvas { position: relative; width: 1200px; height: 644px; }

  .package { position: absolute; top: 65px; width: 485px; height: 492px; }
  .package--blueberry { left: 93px; --accent: var(--blueberry); }
  .package--cherry { left: 625px; --accent: var(--cherry); }

  .package__lid {
    position: absolute; left: 0; top: 0; width: 485px; height: 42px;
    background: var(--lid); box-shadow: 0 2px 4px var(--shadow); z-index: 2;
  }
  .package__body {
    position: absolute; left: 6px; top: 42px; width: 475px; height: 450px;
    background: var(--body); box-shadow: 0 2px 6px var(--shadow);
  }

  .label-art { position: absolute; left: 0; top: 0; z-index: 1; }
  .brand-name {
    font-family: "Jost", sans-serif; font-weight: 300; font-size: 48px;
    fill: var(--white);
  }
  .product-name {
    font-family: "Jost", sans-serif; font-weight: 300; font-size: 30px;
    fill: var(--white);
  }

  .tile {
    position: absolute; width: 67px; height: 42px; background: var(--white);
    box-shadow: 2px 3px 4px var(--shadow); z-index: 1;
  }
  .tile--accent { background: var(--accent); }

  .weight {
    position: absolute; left: 291px; top: 425px; width: 156px; height: 42px;
    background: var(--accent); box-shadow: 2px 3px 4px var(--shadow); z-index: 1;
    font-family: "Ubuntu Mono", monospace; font-size: 22px; color: var(--white);
    display: flex; align-items: center; justify-content: center; letter-spacing: 1px;
  }
</style>
</head>
<body>
<main class="canvas">

  <section class="package package--blueberry">
    <div class="package__lid"></div>
    <div class="package__body"></div>
    <svg class="label-art" width="485" height="492">
      <defs>
        <linearGradient id="blueberryTone" x1="0" y1="0" x2="1" y2="1">
          <stop offset="0" stop-color="#5a3a4c"/>
          <stop offset="0.5" stop-color="#2e2230"/>
          <stop offset="1" stop-color="#6b3645"/>
        </linearGradient>
      </defs>
      <polygon role="img" aria-label="Window showing freeze dried blueberries" points="202,305 447,305 447,467 113,467 113,365 202,365" fill="url(#blueberryTone)"/>
      <text class="brand-name" transform="translate(77,264) rotate(-90)" text-anchor="middle" textLength="400" lengthAdjust="spacingAndGlyphs">MARISOL &amp; JOCELYN FRUIT CO</text>
      <text class="product-name" x="120" y="105" textLength="237" lengthAdjust="spacingAndGlyphs">Freeze Dried Blueberries</text>
    </svg>
    <div class="tile tile--accent" style="left:381px;top:65px"></div>
    <div class="tile" style="left:291px;top:125px"></div>
    <div class="tile" style="left:381px;top:125px"></div>
    <div class="tile" style="left:202px;top:185px"></div>
    <div class="tile tile--accent" style="left:291px;top:185px"></div>
    <div class="tile" style="left:381px;top:185px"></div>
    <div class="tile" style="left:202px;top:245px"></div>
    <div class="tile" style="left:291px;top:245px"></div>
    <div class="tile tile--accent" style="left:381px;top:245px"></div>
    <div class="weight">500 grams</div>
  </section>

  <section class="package package--cherry">
    <div class="package__lid"></div>
    <div class="package__body"></div>
    <svg class="label-art" width="485" height="492">
      <defs>
        <linearGradient id="cherryTone" x1="0" y1="0" x2="1" y2="1">
          <stop offset="0" stop-color="#a02a3c"/>
          <stop offset="0.5" stop-color="#7a1a2c"/>
          <stop offset="1" stop-color="#b8394a"/>
        </linearGradient>
      </defs>
      <polygon role="img" aria-label="Window showing freeze dried cherries" points="202,305 447,305 447,467 113,467 113,365 202,365" fill="url(#cherryTone)"/>
      <text class="brand-name" transform="translate(77,264) rotate(-90)" text-anchor="middle" textLength="400" lengthAdjust="spacingAndGlyphs">MARISOL &amp; JOCELYN FRUIT CO</text>
      <text class="product-name" x="120" y="105" textLength="238" lengthAdjust="spacingAndGlyphs">Freeze Dried Cherries</text>
    </svg>
    <div class="tile tile--accent" style="left:381px;top:65px"></div>
    <div class="tile" style="left:291px;top:125px"></div>
    <div class="tile" style="left:381px;top:125px"></div>
    <div class="tile" style="left:202px;top:185px"></div>
    <div class="tile tile--accent" style="left:291px;top:185px"></div>
    <div class="tile" style="left:381px;top:185px"></div>
    <div class="tile" style="left:202px;top:245px"></div>
    <div class="tile" style="left:291px;top:245px"></div>
    <div class="tile tile--accent" style="left:381px;top:245px"></div>
    <div class="weight">500 grams</div>
  </section>

</main>
</body>
</html>
```